Double sided flyer for industrial investment firm

We need a A4 double sided flyer (1 page, see attached draft), which we will fold in the midle. Text is attached. What is missing is a professional and clean looking design. Text length can not be changed. it is all in German, but that should not influence the design. The flyer is added to a letter which we send to small industrial companies as an introduction to us as an investor.

What is important?
- No fancy, colorful and funny designs.
- We want a clean, professional almost minimalist design. it does not take much design elements.
- Format either landscape or vertical, whatever works best.
- stay with the colors of our company (grey, blue). see www.velmora-ag.ch for details.
- Currently used graphic in the document should be used, but is not a must. Otherwise stay with pictures or Swiss Alps (if more pictures are needed). will upload some pictures as examples.

Format for the finished flyer: InDesign and Word document or similar.
Updates

The flyer will be folded in the middle so that it becomes A5. all current designs work only as a A4 format. An A4 folded has basically 4 pages, each being A5 size. Please adapt the design accordingly.

Target Market(s)

Owners of small to medium industrial companies in Switzerland

Industry/Entity Type

Industrial

Font styles to use
Serif
Sans Serif

Colors
0255a3
3276b5
85abd2
cedeed

Requirements
Must have
• 1 page, double sided. folded in the middle. A4 Format

```html
<!DOCTYPE html>
<html lang="de">
<head>
<meta charset="utf-8">
<title>Fragen und Antworten zu Velmora</title>
<link rel="stylesheet" href="https://fonts.googleapis.com/css2?family=Ubuntu:wght@300;500;700&family=Cinzel:wght@500&display=swap">
<style>
  :root {
    --navy: #2e3786;
    --blue-deep: #0255a3;
    --blue-mid: #3276b5;
    --blue-light: #85abd2;
    --blue-pale: #cedeed;
    --sky-top: #2d6ab2;
    --sky-low: #8fb6df;
    --snow: #eef2f7;
    --snow-shade: #c6d4e6;
    --paper: #ececec;
    --text-grey: #5a5a5a;
    --white: #ffffff;
  }
  html, body {
    margin: 0;
    padding: 0;
    overflow: hidden;
    background: var(--white);
  }
  .cover {
    position: relative;
    width: 846px;
    height: 1200px;
    overflow: hidden;
    background: var(--paper);
    font-family: "Ubuntu", sans-serif;
  }
  .alpine-photo {
    position: absolute;
    left: 0;
    top: 0;
    width: 846px;
    height: 950px;
    background: linear-gradient(180deg,
      var(--sky-top) 0%,
      #4d86c6 18%,
      var(--sky-low) 33%,
      #d9e5f2 37%,
      var(--snow) 40%,
      var(--snow-shade) 48%,
      #e4ebf4 54%,
      var(--snow-shade) 62%,
      #a9bdd6 70%,
      var(--snow) 78%,
      #f3f6fa 100%);
  }
  .cover-shapes {
    position: absolute;
    inset: 0;
    width: 846px;
    height: 1200px;
  }
  .brand {
    position: absolute;
    top: 88px;
    right: 84px;
    text-align: right;
  }
  .brand-name {
    display: flex;
    align-items: center;
    justify-content: flex-end;
    gap: 10px;
    font-family: "Cinzel", serif;
    font-weight: 500;
    font-size: 28px;
    letter-spacing: 1px;
    color: var(--navy);
    line-height: 1;
  }
  .brand-mark {
    width: 14px;
    height: 14px;
    background: var(--navy);
  }
  .brand-url {
    margin-top: 14px;
    font-weight: 500;
    font-size: 17px;
    letter-spacing: 0.5px;
    color: var(--white);
  }
  .title {
    position: absolute;
    left: 205px;
    top: 988px;
    margin: 0;
  }
  .title-lead {
    display: block;
    font-weight: 300;
    font-size: 30px;
    color: var(--text-grey);
    letter-spacing: -0.3px;
    line-height: 1.2;
  }
  .title-main {
    display: block;
    margin-top: 16px;
    font-weight: 700;
    font-size: 51px;
    color: var(--blue-deep);
    letter-spacing: -1.5px;
    line-height: 1;
  }
</style>
</head>
<body>
  <main class="cover">
    <div class="alpine-photo" role="img" aria-label="Photo: panorama of snow-covered Swiss Alps under a clear blue sky, with a groomed ski slope and lift masts in the foreground"></div>

    <svg class="cover-shapes" viewBox="0 0 1000 1419" preserveAspectRatio="none" aria-hidden="true">
      <path class="wave-band" fill="var(--navy)"
        d="M0 718 C90 700 150 760 185 880 C215 990 250 1100 300 1110 C380 1120 460 990 620 945 C760 905 900 895 1000 905 L1000 975 C880 950 760 975 620 1010 C480 1045 380 1120 300 1112 C250 1105 220 1030 195 930 C170 850 100 815 0 825 Z"/>
      <path class="paper" fill="var(--paper)"
        d="M0 825 C100 815 170 850 195 930 C220 1030 250 1105 300 1112 C380 1120 480 1045 620 1010 C760 975 880 950 1000 975 L1000 1419 L0 1419 Z"/>
    </svg>

    <header class="brand">
      <div class="brand-name"><span class="brand-mark"></span>VELMORA</div>
      <div class="brand-url">www.velmora-ag.ch</div>
    </header>

    <h1 class="title">
      <span class="title-lead">Fragen und</span>
      <span class="title-main">Antworten zu Velmora</span>
    </h1>
  </main>
</body>
</html>
```